Project Manager Business Card for Top Architectural Firm

Update and design a stunning Senior Project Manager Business Card

MARCO T. DRUMMOND II
Senior Project Manager

H A L C Y O N
A R C H I T E C T U R E L L C.
www.HalcyonGrandEstates.example
4127 NW 52nd Ter. Suite 2308
Miami, FL 33148
C: (305) 555-0184
mdrummond.halcyongrandestates@mailbox.example

Looking to have the logo to be UV Spot ink printed and to be prominent.

Target Market(s)

High end real estate architecture construction

Industry/Entity Type

Architect

Contact Information for Business Card

MARCO T. DRUMMOND II
Senior Project Manager

H A L C Y O N
Miami, FL 33148
C: (305) 555-0184

Font styles to use
Sans Serif

Colors

Designer to choose colors to be used in the design.

Requirements
Must have
• Prominent Logo

```html
<!DOCTYPE html>
<html lang="en">
<head>
<meta charset="utf-8">
<title>Halcyon Architecture LLC — Business Card</title>
<link href="https://fonts.googleapis.com/css2?family=Exo+2:wght@300;400;500&family=Saira+Condensed:wght@300;400&display=swap" rel="stylesheet">
<style>
  :root {
    --stage: #e9e7e3;
    --card-white: #ffffff;
    --card-black: #141414;
    --ink: #1c1c1c;
    --ink-soft: #3a3a3a;
    --rule: #4a4a4a;
    --accent-red: #d2432f;
    --accent-blue-dark: #2f4f8f;
    --accent-blue-light: #7fc0e6;
    --logo-light: #f2f2f2;
  }
  * { box-sizing: border-box; margin: 0; padding: 0; }
  html, body {
    width: 1200px; height: 800px; overflow: hidden;
    background: var(--stage);
  }
  .stage {
    width: 1200px; height: 800px;
    display: flex; align-items: center; justify-content: center; gap: 56px;
  }
  .card {
    width: 540px; height: 310px; position: relative; overflow: hidden;
    box-shadow: 0 10px 28px rgba(0,0,0,.18);
  }
  /* Front */
  .card--front { background: var(--card-white); color: var(--ink); }
  .brand {
    position: absolute; left: 24px; top: 72px; width: 170px;
    display: flex; flex-direction: column; align-items: center; gap: 12px;
  }
  .brand__mark {
    width: 46px; height: 46px; border-radius: 50%;
    background: var(--accent-blue-dark);
  }
  .brand__name {
    font-family: "Exo 2", sans-serif; font-weight: 300;
    text-align: center; line-height: 1.6; white-space: nowrap;
  }
  .brand__name .line-1 { display: block; font-size: 21px; letter-spacing: 1px; }
  .brand__name .line-2 { display: block; font-size: 7.5px; letter-spacing: 1px; }
  .brand__name .line-2 .suffix { margin-left: 5px; }
  .divider {
    position: absolute; left: 210px; top: 58px; width: 1px; height: 150px;
    background: var(--rule);
  }
  .person { position: absolute; left: 230px; top: 64px; right: 16px; }
  .person__name {
    font-family: "Saira Condensed", sans-serif; font-weight: 400;
    font-size: 30px; letter-spacing: .5px; line-height: 1; white-space: nowrap;
  }
  .person__title {
    font-family: "Exo 2", sans-serif; font-weight: 400;
    font-size: 11px; letter-spacing: 2px; text-transform: uppercase;
    margin-top: 8px; color: var(--ink-soft); white-space: nowrap;
  }
  .contact { list-style: none; margin-top: 18px; }
  .contact li {
    display: flex; align-items: center; gap: 8px;
    font-family: "Exo 2", sans-serif; font-size: 10.5px; color: var(--ink);
    margin-bottom: 7px; white-space: nowrap;
  }
  .contact svg { width: 11px; height: 11px; flex: none; }
  .address {
    position: absolute; left: 34px; bottom: 34px;
    font-family: "Exo 2", sans-serif; font-size: 10.5px; letter-spacing: .5px;
    text-transform: uppercase; color: var(--ink); white-space: nowrap;
  }
  .edge-band {
    position: absolute; left: 0; right: 0; bottom: 0; height: 10px;
    background: linear-gradient(90deg, var(--accent-blue-dark), var(--accent-blue-light));
  }
  /* Back */
  .card--back {
    background: var(--card-black); color: var(--logo-light);
    display: flex; flex-direction: column; align-items: center; justify-content: center; gap: 16px;
  }
  .card--back .brand__mark { width: 60px; height: 60px; }
  .card--back .brand__name .line-1 { font-size: 34px; letter-spacing: 4px; }
  .card--back .brand__name .line-2 { font-size: 11px; letter-spacing: 3px; }
  .card--back .brand__name .line-2 .suffix { margin-left: 8px; }
</style>
</head>
<body>
<main class="stage">
  <section class="card card--front" aria-label="Business card front">
    <div class="brand">
      <span class="brand__mark" aria-hidden="true"></span>
      <p class="brand__name"><span class="line-1">H A L C Y O N</span><span class="line-2">A R C H I T E C T U R E <span class="suffix">L L C.</span></span></p>
    </div>
    <div class="divider"></div>
    <div class="person">
      <h1 class="person__name">MARCO T. DRUMMOND II</h1>
      <p class="person__title">Senior Project Manager</p>
      <ul class="contact">
        <li>
          <svg viewBox="0 0 12 12" aria-hidden="true"><rect x="3" y="0.5" width="6" height="11" rx="1.2" fill="none" stroke="var(--accent-red)" stroke-width="1.2"/><line x1="5" y1="9.5" x2="7" y2="9.5" stroke="var(--accent-red)" stroke-width="1"/></svg>
          (305) 555-0184
        </li>
        <li>
          <svg viewBox="0 0 12 12" aria-hidden="true"><rect x="0.5" y="2" width="11" height="8" fill="var(--accent-red)"/><polyline points="0.5,2 6,7 11.5,2" fill="none" stroke="#fff" stroke-width="1"/></svg>
          mdrummond.halcyongrandestates@mailbox.example
        </li>
        <li>
          <svg viewBox="0 0 12 12" aria-hidden="true"><circle cx="6" cy="6" r="5.3" fill="none" stroke="var(--accent-red)" stroke-width="1.1"/><ellipse cx="6" cy="6" rx="2.3" ry="5.3" fill="none" stroke="var(--accent-red)" stroke-width="0.9"/><line x1="0.7" y1="6" x2="11.3" y2="6" stroke="var(--accent-red)" stroke-width="0.9"/></svg>
          www.HalcyonGrandEstates.example
        </li>
      </ul>
    </div>
    <p class="address">4127 NW 52nd Ter. Suite 2308, Miami, FL 33148</p>
    <div class="edge-band"></div>
  </section>

  <section class="card card--back" aria-label="Business card back">
    <span class="brand__mark" aria-hidden="true"></span>
    <p class="brand__name"><span class="line-1">H A L C Y O N</span><span class="line-2">A R C H I T E C T U R E <span class="suffix">L L C.</span></span></p>
  </section>
</main>
</body>
</html>
```